Wealth management Facebook Advertisement

Hello, we are trying to capture more leads to our online booking link through Facebook advertisement. We want an attractive modern design to get more clients and catch the attention of high net-worth clients. We deal with high-net-worth retirees, business owners, farmers, and wealth transfer. We offer high-net-worth client solutions that cover Financial Planning, Retirement and Estate Planning, Investment Planning, Tax Planning, and Insurance Planning. The final design that we would be looking for is modern and eye-catching and makes the prospective clients want to click our meeting link to schedule an introductory consultation.

We are in the Wealth Management / Financial Planning industry

Our online booking link Is the following :

https://calendar.bookvantor.net/owa/calendar/CarlMorrowPartnersVLPrivateWealth@velmoracapital.net/bookings/

Our current Facebook page is the following:

https://www.socialquelt.net/MorrowPrivateWealth

Please ask any further questions for needed information for creating design

```html
<!DOCTYPE html>
<html lang="en">
<head>
<meta charset="utf-8">
<title>Your Personal Financial Planner – Carl Morrow &amp; Partners</title>
<link rel="stylesheet" href="https://fonts.googleapis.com/css2?family=Barlow:wght@500;600&display=swap">
<style>
  :root {
    --navy: #1b2863;
    --navy-deep: #142152;
    --blue-mid: #13407a;
    --blue-band: #1a5290;
    --royal: #2c56b8;
    --orange: #ff8f12;
    --amber: #ffb81c;
    --title-yellow: #d6dc00;
    --accent-yellow: #f4ea00;
    --white: #ffffff;
    --ink: #14204a;
    --brand-blue: #3466d6;
    --logo-navy: #1b2a5e;
    --pill: #e9edf3;
  }
  * { margin: 0; padding: 0; box-sizing: border-box; }
  html, body { width: 1200px; height: 457px; overflow: hidden; background: var(--navy); }
  .banner {
    position: relative; width: 1200px; height: 457px; overflow: hidden;
    background: var(--navy);
    font-family: "Barlow", Arial, sans-serif; color: var(--white);
  }
  .backdrop { position: absolute; inset: 0; }
  .headline { position: absolute; left: 63px; top: 48px; font-weight: 500; line-height: 1; }
  .headline__lead { display: block; font-size: 54px; letter-spacing: 0.5px; }
  .headline__main { display: block; font-size: 70px; margin-top: 8px; letter-spacing: 0.5px; }
  .headline__accent { color: var(--title-yellow); font-weight: 600; }
  .services {
    position: absolute; left: 65px; top: 193px; width: 520px;
    font-size: 19.5px; font-weight: 500; line-height: 25px; letter-spacing: 0.2px;
  }
  .services__hl { color: var(--accent-yellow); font-weight: 600; }
  .advisor-visual {
    position: absolute; left: 88px; top: 288px; width: 254px; height: 169px;
    border-radius: 127px 127px 0 0;
    background: linear-gradient(180deg, #f6e35c 0%, #f3dd45 100%);
  }
  .skyline-photo {
    position: absolute; inset: 0;
    clip-path: polygon(915px 0, 1200px 0, 1200px 457px, 927px 457px, 689px 226px);
    background: linear-gradient(180deg, #8fb7dd 0%, #c9c7c0 30%, #e8b980 42%, #3f3a33 52%, #2b2a26 62%, #7b6e58 75%, #c9a46f 100%);
  }
  .brand { position: absolute; left: 884px; top: 52px; }
  .brand__name {
    display: flex; align-items: center; gap: 8px;
    color: var(--logo-navy); font-weight: 600; font-size: 20px; letter-spacing: 0.4px; line-height: 1.05;
  }
  .brand__mark { width: 36px; height: 36px; background: var(--logo-navy); flex: none; }
  .brand__firm {
    margin: 10px 0 0 66px; color: var(--brand-blue);
    font-weight: 600; font-size: 21px; line-height: 21px; letter-spacing: 0.4px;
  }
  .web-pill {
    position: absolute; left: 958px; top: 410px; width: 210px; height: 32px;
    border-radius: 16px; background: var(--pill);
    color: var(--ink); font-size: 14.5px; font-weight: 500; letter-spacing: 0.3px;
    display: flex; align-items: center; justify-content: center;
  }
</style>
</head>
<body>
<main class="banner">
  <svg class="backdrop" width="1200" height="457" viewBox="0 0 1200 457" aria-hidden="true">
    <polygon points="0,0 70,0 0,60" fill="var(--navy-deep)"/>
    <polygon points="0,0 80,40 0,115" fill="#17295b"/>
    <polygon points="255,0 610,0 520,110 420,110" fill="var(--blue-mid)"/>
    <polygon points="420,0 915,0 689,226 560,330" fill="var(--blue-mid)"/>
    <polygon points="560,80 650,95 645,195 600,195" fill="var(--blue-band)" opacity="0.6"/>
    <polygon points="593,88 648,140 593,195 538,140" fill="#1d4c88" opacity="0.7"/>
    <polygon points="540,200 590,245 545,270 495,225" fill="#1b4784" opacity="0.6"/>
    <polygon points="0,250 50,298 0,347" fill="var(--blue-mid)"/>
    <polyline points="410,40 492,122 615,0" fill="none" stroke="#c9cdd6" stroke-width="1.6"/>
    <polyline points="0,249 49,298 0,347" fill="none" stroke="var(--orange)" stroke-width="1.6"/>
    <polygon points="635,70 648,70 660,81 648,92 635,92 647,81" fill="var(--orange)"/>
    <polygon points="663,70 676,70 688,81 676,92 663,92 675,81" fill="var(--orange)"/>
    <polygon points="691,70 704,70 716,81 704,92 691,92 703,81" fill="var(--orange)"/>
    <polygon points="689,226 927,457 461,457" fill="var(--amber)"/>
    <polygon points="689,226 927,457 830,457" fill="var(--orange)"/>
    <polygon points="570,340 660,430 630,457 545,457 520,430" fill="#ffc43a" opacity="0.55"/>
    <polyline points="382,457 441,398 501,457" fill="none" stroke="#d3d6dc" stroke-width="9"/>
  </svg>

  <div class="skyline-photo" role="img" aria-label="City skyline at sunset reflected in a calm river"></div>

  <svg class="backdrop" width="1200" height="457" viewBox="0 0 1200 457" aria-hidden="true">
    <polygon points="1076,0 1200,0 1200,30 1169,96" fill="var(--orange)"/>
    <polygon points="1100,0 1190,0 1169,55" fill="var(--amber)"/>
    <polygon points="848,347 960,457 741,457" fill="var(--royal)"/>
    <polygon points="848,395 910,457 786,457" fill="#224aa8"/>
  </svg>

  <h1 class="headline">
    <span class="headline__lead">Your Personal</span>
    <span class="headline__main"><span class="headline__accent">Financial</span> Planner</span>
  </h1>

  <p class="services">
    <span class="services__hl">Financial Planning,</span> Retirement and Estate Planning,
    Investment Planning, <span class="services__hl">Tax Planning,</span>
    and Insurance Planning
  </p>

  <div class="advisor-visual" role="img" aria-label="Illustration of a financial advisor reviewing charts, documents and coins"></div>

  <div class="brand">
    <div class="brand__name"><span class="brand__mark"></span><span>VELMORA<br>PRIVATE WEALTH</span></div>
    <div class="brand__firm">CARL MORROW<br>&amp; PARTNERS</div>
  </div>

  <a class="web-pill">carlmorrowpartners.ca</a>
</main>
</body>
</html>
```